We need business cards for Tarnwick Consulting. We have a logo that was recently designed. I would obviously like the logo on the card and to stay with similar fonts and colors.

I think the font is Trebuchet MS or something very close to it.
CMYK for the blue is C:100 M:100 Y:0 K:0
And for the green C:40 M:0 Y:40 K:0

Tarnwick Consulting is based in Wellington, New Zealand. Doing consulting and advisory work in Australia, PNG and NZ to government and private organisations.
We provide management guidance and consultancy on petroleum, gas and mineral (predominantly gold) projects. (Geophysical consulting).
We advise on design, contractor selection, tendering, risk assessment through to full project delivery and operational management

We are looking for a professional, corporate looking cards.

Industry/Entity Type

Business

```html
<!DOCTYPE html>
<html lang="en">
<head>
<meta charset="utf-8">
<title>Tarnwick Consulting – Business Cards</title>
<link href="https://fonts.googleapis.com/css2?family=Ubuntu:wght@400;500;700&display=swap" rel="stylesheet">
<style>
  :root {
    --backdrop: #e4e2df;
    --charcoal: #22272c;
    --paper: #ffffff;
    --brand-blue: #2e3192;
    --brand-green: #9ac43c;
    --muted: #6d6f73;
    --light-text: #f2f2f2;
  }
  * { box-sizing: border-box; margin: 0; padding: 0; }
  html, body {
    width: 1200px; height: 852px; overflow: hidden;
    background: var(--backdrop);
    font-family: "Ubuntu", "Trebuchet MS", sans-serif;
  }
  .stage { position: relative; width: 1200px; height: 852px; }

  .card {
    position: absolute; top: 256px;
    width: 542px; height: 325px;
    box-shadow: 4px 5px 10px rgba(0,0,0,0.35);
    overflow: hidden;
  }

  /* Front */
  .card--front { left: 62px; background: var(--charcoal); }
  .front-band {
    position: absolute; left: 0; right: 0; top: 104px; height: 116px;
    background: var(--paper);
    border-top: 3px solid var(--brand-green);
    border-bottom: 3px solid var(--brand-green);
  }

  .brand { position: absolute; display: flex; align-items: center; }
  .brand__dot {
    width: 40px; height: 40px; border-radius: 50%;
    background: var(--brand-blue); margin-right: 10px; flex: none;
  }
  .brand__rule { width: 1px; height: 44px; background: var(--brand-green); margin-right: 10px; }
  .brand__name { font-size: 24px; font-weight: 400; color: var(--brand-blue); line-height: 1.05; }
  .brand__tagline { font-size: 13px; color: var(--muted); letter-spacing: 0.6px; margin-top: 2px; }

  .card--front .brand { left: 146px; top: 28px; }

  /* Back */
  .card--back { left: 631px; background: var(--paper); }
  .card--back .brand { left: 34px; top: 55px; }
  .card--back .brand__name { font-size: 22px; }
  .card--back .brand__tagline { font-size: 12.5px; }

  .back-divider {
    position: absolute; left: 0; right: 0; top: 158px; height: 5px;
    border-top: 2px solid var(--brand-blue);
    border-bottom: 1px solid var(--brand-blue);
    background: var(--paper);
  }
  .back-panel {
    position: absolute; left: 0; right: 0; top: 163px; bottom: 0;
    background: var(--charcoal);
  }

  .person { position: absolute; left: 23px; top: 51px; }
  .person__name { font-size: 25px; font-weight: 700; color: var(--brand-green); letter-spacing: 0.5px; }
  .person__role { font-size: 15px; color: var(--light-text); margin-top: 3px; }

  .contact { position: absolute; left: 296px; top: 21px; list-style: none; color: var(--light-text); font-size: 13.5px; }
  .contact__item { display: flex; align-items: center; height: 27px; }
  .contact__icon { width: 16px; height: 16px; margin-right: 10px; flex: none; }
  .contact__address { line-height: 18px; margin-top: 1px; }
</style>
</head>
<body>
<main class="stage">

  <section class="card card--front" aria-label="Card front">
    <div class="front-band">
      <div class="brand">
        <span class="brand__dot"></span>
        <span class="brand__rule"></span>
        <div>
          <div class="brand__name">Tarnwick Consulting</div>
          <div class="brand__tagline">We provide geophysical consulting</div>
        </div>
      </div>
    </div>
  </section>

  <section class="card card--back" aria-label="Card back">
    <div class="brand">
      <span class="brand__dot"></span>
      <span class="brand__rule"></span>
      <div>
        <div class="brand__name">Tarnwick Consulting</div>
        <div class="brand__tagline">We provide geophysical consulting</div>
      </div>
    </div>

    <div class="back-divider"></div>

    <div class="back-panel">
      <div class="person">
        <div class="person__name">Helen Marsh</div>
        <div class="person__role">Director</div>
      </div>

      <ul class="contact">
        <li class="contact__item">
          <svg class="contact__icon" viewBox="0 0 16 16" aria-hidden="true">
            <path d="M4 1.5l2.2 3-1.4 1.6c.8 1.8 2.2 3.3 4 4.2l1.6-1.4 3 2.2-1.2 2.6C6.8 13.5 2.3 9 1.4 2.7z" fill="var(--brand-green)"/>
          </svg>
          +64 4 555 0182
        </li>
        <li class="contact__item">
          <svg class="contact__icon" viewBox="0 0 16 16" aria-hidden="true">
            <rect x="1" y="3" width="14" height="10" fill="var(--brand-green)"/>
            <path d="M1 3l7 5.5L15 3" fill="none" stroke="var(--charcoal)" stroke-width="1.3"/>
          </svg>
          Helen@tarnwickconsulting.co.nz
        </li>
        <li class="contact__item">
          <svg class="contact__icon" viewBox="0 0 16 16" aria-hidden="true">
            <g fill="none" stroke="var(--brand-green)" stroke-width="2.2" stroke-linecap="round">
              <path d="M7 9.5L4.8 11.7a2.2 2.2 0 01-3.1-3.1L4.4 6a2.2 2.2 0 013.1 0"/>
              <path d="M9 6.5l2.2-2.2a2.2 2.2 0 013.1 3.1L11.6 10a2.2 2.2 0 01-3.1 0"/>
            </g>
          </svg>
          www.tarnwickconsulting.co.nz
        </li>
        <li class="contact__address">14 Tarrow Way Brookmere 6071<br>Wellington, New Zealand</li>
      </ul>
    </div>
  </section>

</main>
</body>
</html>
```